Flyer/Poster Tischtennis Sportverein
Zielgruppe
Tischtennisverein - Zielgruppe: Kinder von 8 - 12 Jahren
Aufgabenstellung
Allgemeiner Flyer für Tischtennisverein - Werbung für Kindertraining, Texbereich sollte im Design enthalten sein, aber so gestaltet dass der Text je nach Bedarf durch uns angepasst werden kann
DIN Format: Sollte als Postkartenformat sowie als DIN A3 oder DIN A2 Poster zu verwenden
Angehängtes Logo einbinden aber nicht zu prominent

```html
<!DOCTYPE html>
<html lang="de">
<head>
<meta charset="utf-8">
<title>Kindertraining – Flyer</title>
<link href="https://fonts.googleapis.com/css2?family=Bebas+Neue&family=Open+Sans:wght@400;600&display=swap" rel="stylesheet">
<style>
  :root {
    --page-bg: #f1f1f1;
    --green-light: #a9cf7e;
    --green-mid: #7cb23d;
    --green-deep: #0f6d35;
    --green-hill: #b6d48c;
    --paper: #ececec;
    --ink: #1a1a1a;
    --pink: #de6680;
    --paddle: #d4114f;
    --teal-dark: #075a66;
    --teal: #00a1b8;
    --teal-light: #6cbfca;
    --white: #ffffff;
  }
  * { margin: 0; padding: 0; box-sizing: border-box; }
  html, body {
    width: 1200px; height: 720px; overflow: hidden;
    background: var(--page-bg);
  }
  .flyer {
    position: absolute; left: 365px; top: 30px;
    width: 470px; height: 660px; overflow: hidden;
    background: linear-gradient(160deg, var(--green-light) 0%, var(--green-mid) 45%, var(--green-mid) 100%);
  }
  .flyer-shapes { position: absolute; inset: 0; }
  .info-circle {
    position: absolute; left: 92px; top: 60px;
    width: 330px; height: 330px; border-radius: 50%;
    background: var(--paper);
    box-shadow: 0 4px 18px rgba(0,0,0,.18);
  }
  .info-content {
    position: absolute; left: 128px; top: 118px; width: 272px;
    color: var(--ink);
  }
  .info-title {
    font-family: 'Bebas Neue', sans-serif; font-size: 30px;
    letter-spacing: 1.5px; line-height: 1; margin-bottom: 6px;
  }
  .info-text {
    font-family: 'Open Sans', sans-serif; font-size: 12px; line-height: 1.42;
  }
  .info-date {
    display: inline-block; margin-top: 12px;
    background: var(--pink); color: var(--white);
    font-family: 'Open Sans', sans-serif; font-weight: 600; font-size: 12px;
    padding: 7px 44px 7px 10px;
  }
  .paddles-art {
    position: absolute; left: 12px; top: 120px; width: 120px; height: 300px;
    border-radius: 60px;
    background: linear-gradient(180deg, rgba(212,17,79,.55), rgba(212,200,180,.5));
  }
  .table-art {
    position: absolute; left: 0; top: 438px; width: 470px; height: 140px;
    background: linear-gradient(100deg, #9cc41f 0%, #3c8c3a 45%, var(--green-deep) 100%);
  }
  .footer-band {
    position: absolute; left: 0; bottom: 0; width: 470px; height: 100px;
    background: linear-gradient(180deg, var(--teal-dark) 0%, var(--teal) 35%, var(--teal-light) 100%);
  }
  .footer-url {
    position: absolute; left: 108px; bottom: 40px;
    font-family: 'Bebas Neue', sans-serif; font-size: 20px; letter-spacing: 1.5px;
    color: var(--white);
  }
  .club-name {
    position: absolute; right: 18px; bottom: 22px;
    display: flex; align-items: center; gap: 6px;
    font-family: 'Open Sans', sans-serif; font-weight: 600; font-size: 11px;
    color: var(--white);
  }
  .club-name .mark { width: 10px; height: 10px; background: var(--white); }
</style>
</head>
<body>
  <article class="flyer">
    <svg class="flyer-shapes" width="470" height="660" viewBox="0 0 470 660" aria-hidden="true">
      <circle cx="290" cy="60" r="170" fill="var(--green-light)" opacity=".55"/>
      <circle cx="350" cy="260" r="220" fill="none" stroke="var(--green-light)" stroke-width="40" opacity=".35"/>
      <path d="M0 470 C40 300 260 250 340 470 Z" fill="var(--green-hill)"/>
    </svg>

    <div class="paddles-art" role="img" aria-label="Illustration: drei rote Tischtennisschläger mit Ball"></div>

    <div class="info-circle"></div>
    <section class="info-content">
      <h1 class="info-title">Kindertraining</h1>
      <p class="info-text">Sie erinnern sich. Der Blindtext-Fall im vorigen Jahr. Nun will Karl noch nach Canossa. Und Claudia heiratet zur Busse Copperfield. Jeden Morgen entzünden sie eine Kerze. Jeden Nachmittag ist eine Runde Rosenkranz fällig. Zur Heiligen Marie. Weil Karl mit dem Zopf der Claudia mit dem Smile optisch nette Koran-Typo aufs Mieder hat sticken lassen.</p>
      <p class="info-date">am Sa, 16.3.2016, 17:00 Uhr</p>
    </section>

    <div class="table-art" role="img" aria-label="Illustration: grüne Tischtennisplatte mit Netz und Ball"></div>

    <footer class="footer-band">
      <span class="footer-url">www.gruenwiese-tt.de</span>
      <span class="club-name"><span class="mark"></span>SV Grünwiese e.V.</span>
    </footer>
  </article>
</body>
</html>
```